Dermavale "polish what the seasons left you" The whole body approach to beauty, customized skincare a

I need a stronger logo design than what I have now. I currently have a small med spa in Chicago, IL. I will be expanding my brand to New York City and the Hamptons of NY. The services I provide in Chicago include; advanced medical grade skincare treatments, laser, plastic surgery and nutrition counsel. My concept is personalized skincare. Part of my philosophy is to dedicate a lot of time and make myself always available to my clients questions and concerns. To maintain integrity of the Dermavale Philosophy I do not advertise. Dermavale is an "exclusive skincare club" therefore you must be referred by an existing client or staff member in order to get an appointment. My Chicago clientele consists of young professionals competing with their peers to look their absolute best. The New York and Hamptons business has a completely different structure. It is a Mobile med spa service providing treatments at people's homes. The services provided are advanced skincare, wellness, massage, spray tan, hair and makeup. My vision for the new logo design is to exude an image that is both cutting edge, relevant, sophisticated, sexy and modern (sleek) yet practical and strong. It must be eye catching yet simplistic, aesthetically pleasing to look at and above all must promote EXCLUSIVITY! bellow I have attached my current logo design which is printed using silver and gold foil. The other is the logo on my prescription skincare products. I need to merge the two for the brand to be cohesive. I would like to print my business cards on a mirror like material where you can see your reflection. Front of card: the brand Dermavale across the front and across the bottom will be Chicago. New York. Hamptons Back of card: in a font style like writing "Dermavale is the whole body approach to beauty. customized medical grade skincare. massage. wellness counsel. By appointment only
www.dermavalewellness-example.com p: (555) 318-2406
I am open to all suggestions to make my brand as strong as possible. Please be creative and relevant. Thank you!

```html
<!DOCTYPE html>
<html lang="en">
<head>
<meta charset="UTF-8">
<title>Dermavale Business Cards</title>
<link rel="stylesheet" href="https://fonts.googleapis.com/css2?family=Dancing+Script:wght@400&family=Raleway:wght@200;300&display=swap">
<style>
  :root {
    --backdrop: #e9e6e2;
    --card-black: #050505;
    --card-sheen: #8a8a8a;
    --card-white: #ffffff;
    --ink-light: #f4f4f4;
    --ink-muted: #c9c9c9;
    --ink-dark: #3a3a3a;
    --shadow: rgba(0, 0, 0, 0.22);
  }
  * { margin: 0; padding: 0; box-sizing: border-box; }
  html, body {
    width: 1200px;
    height: 646px;
    overflow: hidden;
    background: var(--backdrop);
  }
  .canvas {
    width: 1200px;
    height: 646px;
    display: flex;
    align-items: center;
    justify-content: center;
    gap: 60px;
  }
  .card {
    width: 510px;
    height: 291px;
    position: relative;
    box-shadow: 0 10px 28px var(--shadow);
    overflow: hidden;
  }

  /* Back of card */
  .card--back {
    background: var(--card-white);
    color: var(--ink-dark);
  }
  .card-back__statement {
    position: absolute;
    top: 58px;
    left: 40px;
    right: 40px;
    text-align: center;
    font-family: "Dancing Script", cursive;
    font-size: 21px;
    line-height: 1.45;
  }
  .card-back__appointment {
    display: block;
    margin-top: 2px;
  }
  .card-back__web,
  .card-back__phone {
    position: absolute;
    bottom: 34px;
    font-family: "Raleway", sans-serif;
    font-weight: 300;
    font-size: 14px;
    letter-spacing: 0.3px;
  }
  .card-back__web { left: 34px; }
  .card-back__phone { right: 34px; }

  /* Front of card */
  .card--front {
    background:
      radial-gradient(ellipse 360px 230px at 20% 112%, var(--card-sheen) 0%, #3a3a3a 35%, transparent 75%),
      var(--card-black);
    color: var(--ink-light);
  }
  .card-front__brand {
    position: absolute;
    left: 42px;
    bottom: 118px;
    font-family: "Raleway", sans-serif;
    font-weight: 200;
    font-size: 60px;
    letter-spacing: 1px;
    line-height: 1;
  }
  .card-front__locations {
    position: absolute;
    left: 46px;
    bottom: 86px;
    font-family: "Raleway", sans-serif;
    font-weight: 200;
    font-size: 19px;
    letter-spacing: 1.2px;
    color: var(--ink-muted);
  }
</style>
</head>
<body>
  <main class="canvas">
    <section class="card card--back" aria-label="Back of business card">
      <p class="card-back__statement">
        Dermavale is the whole body approach to beauty, customized medical grade skincare. massage. wellness counsel.
        <span class="card-back__appointment">By appointment only!</span>
      </p>
      <p class="card-back__web">www.dermavalewellness-example.com</p>
      <p class="card-back__phone">p: (555) 318-2406</p>
    </section>

    <section class="card card--front" aria-label="Front of business card">
      <h1 class="card-front__brand">DERMAVALE</h1>
      <p class="card-front__locations">CHICAGO | NEW YORK | HAMPTONS</p>
    </section>
  </main>
</body>
</html>
```